Rack Card for Portuguese Walking Food Tour

I would like a vertical rack card measuring 99x210mm. Here is the information I would like to include. It does not need to be in this format. We are located in Setubal, Portugal.
Please use the attached Teal Heron Logo.
Setúbal: Tradition and Today
Experience the culinary delights of Setúbal, Portugal with a walking food tour around our waterfront village. Discover the Mercado da Gaivota Branca, voted one of the world’s best markets by Metro Ledger, and indulge in local wines and dishes. Prepare for a calm stroll on flat streets. No hills to climb on this tour.
Duration: 4 hours
www.brinebasketwalks.com
+351 265 000 487

```html
<!DOCTYPE html>
<html lang="en">
<head>
<meta charset="utf-8">
<title>Setúbal Walking Food Tour – Rack Card</title>
<link rel="stylesheet" href="https://fonts.googleapis.com/css2?family=Poppins:wght@500;600;700&display=swap">
<style>
  :root {
    --backdrop: #dddddd;
    --paper: #ffffff;
    --orange: #ec6a27;
    --ink-gray: #5f6062;
    --photo-warm: #d9735a;
    --photo-light: #f0c7b5;
  }
  * { box-sizing: border-box; margin: 0; padding: 0; }
  html, body { width: 1200px; height: 1200px; overflow: hidden; }
  body {
    background: var(--backdrop);
    font-family: "Poppins", sans-serif;
    position: relative;
  }
  .rack-card {
    position: absolute;
    left: 414px; top: 206px;
    width: 372px; height: 788px;
    background: var(--paper);
  }
  .brand {
    position: absolute;
    left: 0; right: 0; top: 36px;
    display: flex; align-items: center; justify-content: center; gap: 10px;
  }
  .brand-dot {
    width: 40px; height: 40px; border-radius: 50%;
    background: var(--orange);
  }
  .brand-name {
    font-weight: 600; font-size: 24px; color: var(--ink-gray);
    letter-spacing: 0.2px;
  }
  .tour-panel {
    position: absolute;
    left: 16px; top: 122px;
    width: 340px; height: 561px;
    background: var(--orange);
    border-radius: 19px 19px 0 0;
    color: var(--paper);
  }
  .tour-title {
    position: absolute; left: 0; right: 0; top: 20px;
    text-align: center; font-weight: 700; font-size: 76px; line-height: 1;
    letter-spacing: -0.5px;
  }
  .tour-subtitle {
    position: absolute; left: 0; right: 0; top: 100px;
    text-align: center; font-weight: 600; font-size: 27px; line-height: 1.2;
  }
  .market-photo {
    position: absolute; left: 15px; top: 159px;
    width: 147px; height: 272px; border-radius: 12px;
    background: linear-gradient(160deg, var(--photo-light) 0%, var(--photo-warm) 45%, #c85a3f 70%, var(--photo-light) 100%);
  }
  .info-box {
    position: absolute; left: 172px; width: 148px;
    border-radius: 10px;
    display: flex; align-items: center; justify-content: center;
    text-align: center; font-weight: 500; font-size: 12.3px; line-height: 14.3px;
    padding: 6px 8px;
  }
  .info-box--filled { top: 159px; height: 126px; background: var(--paper); color: var(--orange); }
  .info-box--outline { top: 297px; height: 134px; border: 1.5px solid var(--paper); color: var(--paper); }
  .rule { position: absolute; left: 13px; width: 310px; height: 1.5px; background: var(--paper); }
  .rule--top { top: 450px; }
  .rule--bottom { top: 507px; }
  .terrain-note {
    position: absolute; left: 0; right: 0; top: 455px; text-align: center;
  }
  .terrain-note .lead { display: block; font-weight: 600; font-size: 15.5px; line-height: 21px; }
  .terrain-note .emphasis { display: block; font-weight: 600; font-size: 20.5px; line-height: 25px; }
  .duration {
    position: absolute; left: 0; right: 0; top: 520px;
    text-align: center; font-weight: 600; font-size: 28px; line-height: 1.2;
  }
  .phone {
    position: absolute; left: 0; right: 0; top: 683px;
    text-align: center; color: var(--orange);
    font-weight: 700; font-size: 35px; line-height: 52px; letter-spacing: -0.5px;
  }
  .web-band {
    position: absolute; left: 16px; top: 735px;
    width: 340px; height: 37px;
    background: var(--orange); border-radius: 0 0 19px 19px;
    display: flex; align-items: center; justify-content: center;
    color: var(--paper); font-weight: 600; font-size: 12.5px;
  }
</style>
</head>
<body>
  <main class="rack-card">
    <header class="brand">
      <span class="brand-dot"></span>
      <span class="brand-name">Brine Basket Walks</span>
    </header>

    <section class="tour-panel">
      <h1 class="tour-title">Setúbal</h1>
      <h2 class="tour-subtitle">Tradition and Today</h2>

      <div class="market-photo" role="img" aria-label="Photo of fresh red mullet fish piled on ice at the market"></div>

      <p class="info-box info-box--filled">Experience the culinary delights of Setúbal, Portugal with a walking food tour around our waterfront village.</p>
      <p class="info-box info-box--outline">Discover the Mercado da Gaivota Branca, voted one of the world’s best markets by Metro Ledger, and indulge in local wines and dishes.</p>

      <div class="rule rule--top"></div>
      <p class="terrain-note">
        <span class="lead">Prepare for a calm stroll on flat streets</span>
        <span class="emphasis">No hills to climb on this tour</span>
      </p>
      <div class="rule rule--bottom"></div>

      <p class="duration">Duration: 4 hours</p>
    </section>

    <p class="phone">+351 265 000 487</p>
    <footer class="web-band">www.brinebasketwalks.com</footer>
  </main>
</body>
</html>
```